Gombrevo business card

Based on company logo and website given , to design a business card temple. Slogan "Your furry friends deserves the best"
Color style please refer to our website

```html
<!DOCTYPE html>
<html lang="en">
<head>
<meta charset="utf-8">
<title>Gombrevo business card</title>
<link href="https://fonts.googleapis.com/css2?family=Ubuntu:wght@400;500;700&family=Courgette&display=swap" rel="stylesheet">
<style>
  :root {
    --backdrop: #c9c9c9;
    --forest: #0a2b29;
    --gold: #bfb23a;
    --leaf: #2f7048;
    --leaf-light: #3f8f5a;
    --white: #ffffff;
    --ruby: #c4202b;
  }
  * { margin: 0; padding: 0; box-sizing: border-box; }
  html, body { width: 1200px; height: 900px; overflow: hidden; }
  body {
    background: var(--backdrop);
    font-family: "Ubuntu", sans-serif;
    position: relative;
  }
  .card {
    position: absolute;
    width: 640px;
    height: 366px;
    overflow: hidden;
    box-shadow: 0 6px 14px rgba(0,0,0,0.25);
  }
  /* Back side */
  .card-back {
    left: 330px;
    top: 50px;
    background: var(--forest);
  }
  .card-back .brand-name {
    position: absolute;
    left: 150px;
    top: 108px;
    font-weight: 500;
    font-size: 70px;
    color: var(--gold);
    letter-spacing: -1px;
    line-height: 1;
    white-space: nowrap;
  }
  .card-back .slogan {
    position: absolute;
    left: 150px;
    top: 190px;
    font-family: "Courgette", cursive;
    font-size: 20px;
    color: var(--white);
    white-space: nowrap;
  }
  .card-back .site {
    position: absolute;
    left: 220px;
    top: 262px;
    font-size: 15px;
    letter-spacing: 3px;
    color: var(--white);
    white-space: nowrap;
  }
  .badge { position: absolute; }
  .badge-left { left: 36px; bottom: 18px; }
  .badge-right { right: 20px; top: 150px; }

  /* Front side */
  .card-front {
    left: 170px;
    top: 480px;
    background: var(--white);
  }
  .card-front .panel { position: absolute; inset: 0; }
  .card-front .brand-name {
    position: absolute;
    left: 40px;
    top: 152px;
    font-weight: 500;
    font-size: 56px;
    color: var(--gold);
    letter-spacing: -1px;
    line-height: 1;
    white-space: nowrap;
  }
  .contact {
    position: absolute;
    left: 410px;
    top: 104px;
    color: var(--white);
  }
  .contact .person {
    font-weight: 700;
    font-size: 21px;
    color: var(--leaf);
    letter-spacing: 0.5px;
  }
  .contact .role { font-size: 16px; margin-top: 2px; }
  .contact .address { font-size: 15px; margin-top: 20px; line-height: 1.3; }
  .contact .lines { list-style: none; margin-top: 14px; font-size: 15px; }
  .contact .lines li { display: flex; align-items: center; gap: 7px; line-height: 1.5; }
  .contact .lines svg { width: 14px; height: 14px; flex: none; }
</style>
</head>
<body>

<section class="card card-back">
  <div class="brand-name">Gombrevo</div>
  <div class="slogan">Your furry friends deserves the best</div>
  <div class="site">www.gombrevo.com.au</div>
  <svg class="badge badge-left" width="96" height="96" viewBox="0 0 96 96" role="img" aria-label="Quality seal">
    <circle cx="48" cy="48" r="44" fill="var(--leaf-light)"/>
    <circle cx="48" cy="48" r="32" fill="var(--white)"/>
  </svg>
  <svg class="badge badge-right" width="80" height="80" viewBox="0 0 96 96" role="img" aria-label="Quality seal">
    <circle cx="48" cy="48" r="44" fill="var(--gold)"/>
    <rect x="4" y="38" width="88" height="20" fill="var(--ruby)"/>
  </svg>
</section>

<section class="card card-front">
  <svg class="panel" width="640" height="366" viewBox="0 0 640 366">
    <path d="M358,0 Q412,180 282,366 L640,366 L640,0 Z" fill="var(--forest)"/>
    <path d="M343,14 Q398,186 266,362 Q384,186 343,14 Z" fill="var(--gold)"/>
  </svg>
  <div class="brand-name">Gombrevo</div>
  <div class="contact">
    <div class="person">Daniel Whitford</div>
    <div class="role">Founder / Owner</div>
    <div class="address">4/22 Larkin Street<br>Bramford Vic 3187</div>
    <ul class="lines">
      <li>
        <svg viewBox="0 0 14 14"><rect x="3.5" y="1" width="7" height="12" rx="1.2" fill="none" stroke="var(--leaf-light)" stroke-width="1.2"/></svg>
        +61 03 9000 4172
      </li>
      <li>
        <svg viewBox="0 0 14 14"><path d="M3,1.5 L5.5,4 L4.2,5.5 Q5.5,8.5 8.5,9.8 L10,8.5 L12.5,11 L11,12.5 Q5,12 1.5,3 Z" fill="none" stroke="var(--leaf-light)" stroke-width="1.2"/></svg>
        1800 000 417
      </li>
      <li>
        <svg viewBox="0 0 14 14"><rect x="1" y="3" width="12" height="8" fill="none" stroke="var(--leaf-light)" stroke-width="1.2"/><path d="M1,3 L7,8 L13,3" fill="none" stroke="var(--leaf-light)" stroke-width="1.2"/></svg>
        hello@gombrevo.com.au
      </li>
      <li>
        <svg viewBox="0 0 14 14"><circle cx="7" cy="7" r="5.8" fill="none" stroke="var(--leaf-light)" stroke-width="1.1"/><ellipse cx="7" cy="7" rx="2.5" ry="5.8" fill="none" stroke="var(--leaf-light)" stroke-width="1"/><path d="M1.2,7 H12.8" stroke="var(--leaf-light)" stroke-width="1"/></svg>
        www.gombrevo.com.au
      </li>
    </ul>
  </div>
</section>

</body>
</html>
```